Solar appointment reminder card

We are looking for a new design for our appointment reminder card since we have changed our logo. The card should have the new logo along with space for the employee to hand write the customers appointment date, time, the employees name and phone number.
I've uploaded what our old basic appointment card looked like and our new logo.

The cards should be in a standard business card size and could be horizontal or vertical.

```html
<!DOCTYPE html>
<html lang="en">
<head>
<meta charset="utf-8">
<title>Sunvale Power – Appointment Reminder Card</title>
<link rel="stylesheet" href="https://fonts.googleapis.com/css2?family=Quicksand:wght@500;700&display=swap">
<style>
  :root {
    --stage: #7b8787;
    --card: #ffffff;
    --brand-orange: #f39224;
    --brand-yellow: #fcc21b;
    --label-brown: #c98a3a;
    --heading-brown: #b8772a;
    --rule-grey: #6d6e74;
    --grad-red: #e9433b;
    --grad-orange: #f2922c;
    --grad-yellow: #ffe02a;
    --faint: rgba(243, 146, 36, 0.14);
  }
  * { box-sizing: border-box; margin: 0; padding: 0; }
  html, body {
    width: 1200px; height: 742px; overflow: hidden;
    background: var(--stage);
    font-family: "Quicksand", sans-serif;
  }
  .stage {
    position: relative; width: 1200px; height: 742px;
    display: flex; align-items: center; justify-content: center; gap: 60px;
  }
  .card {
    position: relative; width: 500px; height: 286px;
    background: var(--card); overflow: hidden;
    box-shadow: 0 10px 28px rgba(0,0,0,0.28);
  }

  /* Front */
  .front-brand {
    position: absolute; left: 60px; top: 0; bottom: 0;
    display: flex; align-items: center; gap: 22px;
  }
  .brand-dot {
    width: 86px; height: 86px; border-radius: 50%;
    background: var(--brand-yellow);
  }
  .brand-name {
    font-weight: 700; font-size: 62px; line-height: 0.95;
    color: var(--brand-orange); letter-spacing: 0.5px;
  }
  .front-accent {
    position: absolute; right: 0; bottom: 0; width: 150px; height: 10px;
    background: linear-gradient(90deg, var(--grad-red), var(--grad-orange), var(--grad-yellow));
  }

  /* Back */
  .back-watermark {
    position: absolute; left: 170px; top: 40px;
    font-weight: 700; font-size: 70px; line-height: 0.95;
    color: var(--faint);
  }
  .appointment-heading {
    position: absolute; left: 34px; top: 30px;
    font-weight: 700; font-size: 30px; color: var(--heading-brown);
    letter-spacing: -0.5px;
  }
  .appointment-fields {
    position: absolute; left: 36px; top: 92px;
    list-style: none;
  }
  .appointment-fields li {
    font-weight: 500; font-size: 22px; line-height: 33px;
    color: var(--label-brown);
  }
  .back-rule {
    position: absolute; left: 0; right: 0; bottom: 38px; height: 6px;
    background: var(--rule-grey);
  }
  .back-band {
    position: absolute; left: 0; right: 0; bottom: 0; height: 30px;
    background: linear-gradient(90deg, var(--grad-red), var(--grad-orange) 45%, var(--brand-yellow) 80%, var(--grad-yellow));
  }
</style>
</head>
<body>
  <main class="stage">
    <section class="card card-front" aria-label="Card front">
      <div class="front-brand">
        <span class="brand-dot" aria-hidden="true"></span>
        <p class="brand-name">Sunvale<br>Power</p>
      </div>
      <span class="front-accent" aria-hidden="true"></span>
    </section>

    <section class="card card-back" aria-label="Card back">
      <p class="back-watermark" aria-hidden="true">Sunvale<br>Power</p>
      <h1 class="appointment-heading">Appointment</h1>
      <ul class="appointment-fields">
        <li>Date:</li>
        <li>Time:</li>
        <li>Representative:</li>
        <li>Phone:</li>
      </ul>
      <span class="back-rule" aria-hidden="true"></span>
      <span class="back-band" aria-hidden="true"></span>
    </section>
  </main>
</body>
</html>
```